Bref créative
Brochure design
vantor crew staffing
oil & gas recruitment experts
This company profile will be used to give an introduction about the services and company strategy. Another main objective is to be used for marketing purposes for the company to clients and job seekers in oil and gas
Consulting
Corporate professional looking profile that will provide an introduction for marketing purposes in order to provide new business in the futures
A3 sized page folded once to form an A4 sized brochuer. The conetnt will be on the inside of the brochure. Full colour ideally on white pages
Ai file for Logo (Please use RED & BLUE VERSION)
Please find attached the wording for the brochure
Please use this image on the front page of the Brochure
Please use this or similar image in the brochure
Please use this image or similar image of an African engineer
If you have sufficient space on the page please use t he following imgae of something similar
If you have sufficient space on the brochure please use the attached image or something similar

```html
<!DOCTYPE html>
<html lang="en">
<head>
<meta charset="utf-8">
<title>Vantor Crew Staffing – Company Profile Brochure</title>
<link href="https://fonts.googleapis.com/css2?family=Open+Sans:wght@400;600;700&display=swap" rel="stylesheet">
<style>
  :root{
    --bg:#e9ebee;
    --paper:#ffffff;
    --blue:#1f6fa8;
    --blue-dark:#0f4471;
    --blue-light:#4f97c9;
    --red:#d22a2a;
    --ink:#3c4550;
    --muted:#7d8792;
  }
  *{box-sizing:border-box;margin:0;padding:0}
  html,body{width:1200px;height:792px;overflow:hidden;background:var(--bg);font-family:"Open Sans",Arial,sans-serif;color:var(--ink)}
  .canvas{position:relative;width:1200px;height:792px}
  .spread{position:absolute;top:206px;width:538px;height:380px;display:flex;box-shadow:0 6px 18px rgba(0,0,0,.18)}
  .spread--outside{left:42px}
  .spread--inside{left:620px}
  .page{position:relative;width:269px;height:380px;overflow:hidden;background:var(--paper)}
  .spread-label{position:absolute;top:-26px;left:0;font-size:11px;font-weight:600;color:var(--muted);letter-spacing:.08em;text-transform:uppercase}

  /* back cover */
  .back-cover{background:var(--blue-dark)}
  .back-cover .shape{position:absolute;inset:0}
  .back-contact{position:absolute;left:20px;top:150px;color:#fff;font-size:6px;line-height:1.6}
  .back-contact strong{font-size:7px;font-weight:700}
  .rig-photo{position:absolute;left:0;bottom:0;width:269px;height:140px;background:linear-gradient(180deg,#b7c3cd,#6b7d8c 60%,#3d5062)}

  /* front cover */
  .front-cover .shape{position:absolute;inset:0}
  .brand{position:absolute;left:62px;top:58px;display:flex;align-items:center;gap:6px}
  .brand-mark{width:14px;height:14px;background:var(--red)}
  .brand-name{font-size:15px;font-weight:700;color:var(--blue);line-height:1}
  .brand-tagline{position:absolute;left:82px;top:78px;font-size:6px;color:var(--blue);letter-spacing:.04em}
  .cover-photo{position:absolute;background:linear-gradient(135deg,#c9d3db,#8b9aa6)}
  .cover-photo--engineer{left:150px;top:110px;width:119px;height:96px}
  .cover-photo--team{left:150px;top:212px;width:119px;height:82px;background:linear-gradient(135deg,#d8dde1,#9aa6b0)}
  .cover-photo--crew{left:40px;top:228px;width:104px;height:66px;background:linear-gradient(135deg,#dfe3e6,#a3aeb7)}

  /* inside pages */
  .inside-left .shape{position:absolute;left:0;top:0}
  .content{position:absolute;left:18px;right:18px;font-size:5.2px;line-height:1.55}
  .inside-left .content{top:62px}
  .inside-right .content{top:26px}
  .section-title{font-size:8px;font-weight:700;color:var(--blue);margin-bottom:5px}
  .sub-title{font-size:6px;font-weight:700;color:var(--blue-dark);margin:5px 0 1px}
  .content p{margin-bottom:4px;color:var(--ink)}
  .section-title--spaced{margin-top:9px}
  .inside-right{border-left:1px solid #e3e6ea}
  .service-title{font-size:9px;font-weight:700;color:var(--blue);margin-bottom:8px}
  .service{margin-bottom:9px}
  .service h3{font-size:6.2px;font-weight:700;color:var(--blue-dark);margin-bottom:2px}
  .service p{margin:0}
  .right-band{position:absolute;left:0;bottom:0}
</style>
</head>
<body>
<div class="canvas">

  <section class="spread spread--outside" aria-label="Outside of brochure">
    <span class="spread-label">Outside</span>

    <article class="page back-cover">
      <svg class="shape" width="269" height="380" viewBox="0 0 269 380">
        <polygon points="0,0 269,0 269,60 0,130" fill="#17588d"/>
        <polygon points="0,130 269,60 269,85 0,160" fill="#2a78b2" opacity=".6"/>
      </svg>
      <div class="back-contact">
        <strong>Vantor Crew Staffing</strong><br>
        14 Harbour Lane, Port Dalen<br>
        +00 123 456 7890<br>
        info@vantorcrew.example
      </div>
      <div class="rig-photo" role="img" aria-label="Photo of an offshore drilling rig at sea"></div>
    </article>

    <article class="page front-cover">
      <svg class="shape" width="269" height="380" viewBox="0 0 269 380">
        <polygon points="0,120 269,95 269,310 0,320" fill="#1f6fa8"/>
        <polygon points="0,320 269,310 269,380 0,380" fill="#0f4471"/>
        <polygon points="0,105 269,82 269,95 0,120" fill="#4f97c9"/>
      </svg>
      <div class="brand">
        <span class="brand-mark"></span>
        <span class="brand-name">vantor crew staffing</span>
      </div>
      <div class="brand-tagline">oil &amp; gas recruitment experts</div>
      <div class="cover-photo cover-photo--engineer" role="img" aria-label="Photo of an engineer in a hard hat on site"></div>
      <div class="cover-photo cover-photo--team" role="img" aria-label="Photo of engineers in safety helmets"></div>
      <div class="cover-photo cover-photo--crew" role="img" aria-label="Photo of oil and gas crew at work"></div>
    </article>
  </section>

  <section class="spread spread--inside" aria-label="Inside of brochure">
    <span class="spread-label">Inside</span>

    <article class="page inside-left">
      <svg class="shape" width="269" height="60" viewBox="0 0 269 60">
        <polygon points="0,0 269,0 269,20 0,48" fill="#1f6fa8"/>
        <polygon points="0,48 269,20 269,28 0,58" fill="#4f97c9" opacity=".7"/>
      </svg>
      <div class="content">
        <h2 class="section-title">1 Why choose Vantor Crew Staffing (VCS)</h2>
        <p>We connect skilled oil and gas professionals with operators, contractors and service firms across onshore and offshore projects worldwide.</p>
        <p>Our consultants understand field roles, safety standards and project timelines, so every shortlist matches both skills and site culture.</p>
        <h3 class="sub-title">Our vision</h3>
        <p>To be the most trusted recruitment partner in the energy sector.</p>
        <h3 class="sub-title">Our mission</h3>
        <p>To deliver proven talent quickly, safely and with full compliance.</p>
        <h3 class="sub-title">Our values</h3>
        <p>Integrity, responsiveness, safety and long term partnership guide every placement we make.</p>
        <h2 class="section-title section-title--spaced">2 Our experience</h2>
        <p>Our team has placed engineers, technicians and managers on drilling, production and pipeline projects for clients of every size.</p>
      </div>
    </article>

    <article class="page inside-right">
      <div class="content">
        <h2 class="service-title">Our services include</h2>
        <div class="service">
          <h3>Retained Search</h3>
          <p>A dedicated search for senior and specialist roles, managed from brief to offer with regular progress reports.</p>
        </div>
        <div class="service">
          <h3>Contingency Search</h3>
          <p>Fast access to screened candidates for permanent and contract roles, with fees due only on placement.</p>
        </div>
        <div class="service">
          <h3>Executive Search</h3>
          <p>Confidential headhunting of leaders who can shape strategy, operations and growth in your business.</p>
        </div>
        <div class="service">
          <h3>Contract Staffing</h3>
          <p>Flexible crews for shutdowns, campaigns and peak workloads, with payroll and mobilisation handled by us.</p>
        </div>
      </div>
      <svg class="right-band" width="269" height="30" viewBox="0 0 269 30">
        <polygon points="0,30 0,22 269,6 269,30" fill="#1f6fa8"/>
      </svg>
    </article>
  </section>

</div>
</body>
</html>
```